Banner Ads for Online Poker Promotion

We are an online poker network, the KRX (www.thekrx.eu). We are looking for a small selection of web banner ads for our latest promotion and we are trying crowdsourcing for the first time!

Banner sizes that we need are:
- 196x523 (static .psd and .png)
- 199x129 (static .psd and .png)
- 447x426 (static .psd and .png)
- 500x400 (static .psd and .png)
- 697x167 (static .psd and .png)
- 460x60 (animated .gif)

The promotion name is ‘Late Rush’ and the concept is that a person who enters one of the specified tournaments four or more times during the promotion will win a free ticket to play that tournament again. So effectively a ‘Rush Late, Bag a Seat’ promo. We also are giving away €10,000 in free entries to the tournaments during the promotion. The specific tournaments are called ‘Calm Dawn Out’ and ‘The Sun Deck’ and run daily on our network. The promotion runs October 1 – 31.

Guidelines:

The name of the promotion, ‘Late Rush’, should feature prominently in the banners.

The strap line can be ‘Rush Late, Bag a Seat’ or something that encourages players to ‘take a shot’ at the tournaments.

Our network logo may feature, but is not absolutely necessary.

Examples of past promotional imagery can be found on our website, in particular these pages: http://www.thekrx.eu/promotions/ and http://www.thekrx.eu/promotions/archived-promotions/

We are looking to go in a more modern and risqué direction than the past, in order to stand out from competition which is very bland.

Please do not use common poker imagery – so no cards, chips, suit icons etc – or objects associated with live poker (tables, etc). This sort of imagery is too clichéd.

More like iOS7, less like iOS6

Think glamour, neon, rock music, extreme sports, and the Soft Tide!

If any further guidance is needed please don’t hesitate to ask.

```html
<!DOCTYPE html>
<html lang="en">
<head>
<meta charset="utf-8">
<title>Late Rush – promotion banner</title>
<link rel="stylesheet" href="https://fonts.googleapis.com/css2?family=Arimo:ital,wght@0,400;0,700;1,400;1,700&display=swap">
<style>
  :root {
    --ink: #1d1d1f;
    --band: #0b0b0c;
    --neon-pink: #ff1ea9;
    --white: #ffffff;
    --button-top: #8c78e0;
    --button-bottom: #4e35a8;
    --button-edge: #3c2a86;
    --crowd-dark: #8f979f;
    --crowd-light: #e6e9ec;
    --hand-warm: #c99a82;
  }
  html, body {
    margin: 0;
    padding: 0;
    width: 1200px;
    height: 960px;
    overflow: hidden;
    background: var(--white);
  }
  .banner {
    position: relative;
    width: 1200px;
    height: 960px;
    overflow: hidden;
    font-family: "Arimo", Arial, sans-serif;
  }
  .crowd-backdrop {
    position: absolute;
    inset: 0;
    background:
      radial-gradient(ellipse at 85% 85%, rgba(255,255,255,0.95) 0%, rgba(255,255,255,0.6) 35%, rgba(255,255,255,0) 65%),
      linear-gradient(160deg, var(--crowd-dark) 0%, #b7bec5 45%, var(--crowd-light) 100%);
  }
  .title-band {
    position: absolute;
    left: 0;
    top: 84px;
    width: 1200px;
    height: 144px;
    background: var(--band);
  }
  .promo-title {
    position: absolute;
    left: 30px;
    top: 4px;
    margin: 0;
    font-size: 232px;
    line-height: 1;
    font-weight: 700;
    letter-spacing: 0;
    color: var(--neon-pink);
    -webkit-text-stroke: 3px var(--white);
    paint-order: stroke fill;
    white-space: nowrap;
  }
  .strapline {
    position: absolute;
    right: 53px;
    top: 334px;
    margin: 0;
    font-size: 60px;
    line-height: 1;
    font-weight: 400;
    color: var(--white);
    text-shadow: 0 2px 4px rgba(0,0,0,0.35);
    white-space: nowrap;
  }
  .hand-photo {
    position: absolute;
    left: 0;
    top: 288px;
    width: 430px;
    height: 672px;
    background:
      radial-gradient(ellipse at 45% 40%, var(--hand-warm) 0%, rgba(201,154,130,0.7) 35%, rgba(111,82,72,0.25) 65%, rgba(111,82,72,0) 80%);
  }
  .cta-button {
    position: absolute;
    left: 473px;
    top: 487px;
    width: 675px;
    height: 160px;
  }
  .cta-button svg {
    position: absolute;
    inset: 0;
  }
  .cta-label {
    position: absolute;
    inset: 0;
    display: flex;
    align-items: center;
    justify-content: center;
    padding-left: 34px;
    font-size: 60px;
    font-style: italic;
    font-weight: 400;
    color: var(--white);
    text-decoration: none;
    text-shadow: 0 2px 3px rgba(0,0,0,0.4);
    white-space: nowrap;
  }
  .prize-copy {
    position: absolute;
    right: 38px;
    top: 726px;
    margin: 0;
    text-align: right;
    font-size: 44px;
    line-height: 66px;
    color: var(--ink);
    white-space: nowrap;
  }
  .tournament-names {
    display: block;
    margin-top: 4px;
    font-style: italic;
    font-weight: 700;
    font-size: 43px;
  }
</style>
</head>
<body>
<main class="banner">
  <div class="crowd-backdrop" role="img" aria-label="Faded grid of excited crowd portraits in grey tones"></div>
  <div class="title-band"></div>
  <h1 class="promo-title">Late Rush</h1>
  <p class="strapline">Rush Late, Bag a Seat</p>
  <div class="hand-photo" role="img" aria-label="Raised hand making a rock gesture, wearing a studded black wristband"></div>
  <div class="cta-button">
    <svg width="675" height="160" viewBox="0 0 675 160" aria-hidden="true">
      <defs>
        <linearGradient id="cta-fill" x1="0" y1="0" x2="0" y2="1">
          <stop offset="0" stop-color="#8c78e0"/>
          <stop offset="1" stop-color="#4e35a8"/>
        </linearGradient>
      </defs>
      <path d="M34 9 Q38 2 47 2 L664 2 Q673 2 673 11 L673 149 Q673 158 664 158 L13 158 Q2 158 4 147 Z" fill="url(#cta-fill)" stroke="#3c2a86" stroke-width="2"/>
    </svg>
    <a class="cta-label" href="#">Start Playing Now</a>
  </div>
  <p class="prize-copy">
    €10,000 in free entries to<br>
    the tournaments during the promotion
    <span class="tournament-names">‘Calm Dawn Out’ &amp; ‘The Sun Deck’</span>
  </p>
</main>
</body>
</html>
```